CRPG is needing business cards, and stationary created.

Pixel Forge created a logo for our business, and now we are wanting business cards, and stationary. I have included two designs of the same logo. Please feel free to use them as you want. The name of the company is Cedar Ridge Property Group LLC, the address is 812 NE Willow Ln., Suite 9, the city & state is Bend, Oregon, zip code is 97815, Telephone number is 541-327-4489, Fax number is 541-327-6051, the name on the business card is Carl Whitby CMCA

Industry/Entity Type

Property Management

Contact Information for Business Card

The card needs to look professional. Upscale.

Requirements
Must have
• The colors we are using are on the logo that has been uploaded.

```html
<!DOCTYPE html>
<html lang="en">
<head>
<meta charset="utf-8">
<title>Cedar Ridge Property Group – Business Card Front</title>
<link rel="stylesheet" href="https://fonts.googleapis.com/css2?family=Saira+Semi+Condensed:wght@500;600&display=swap">
<style>
  :root {
    --teal: #178c77;
    --slate: #3a4758;
    --paper: #fdfdfd;
    --white: #ffffff;
  }
  * { margin: 0; padding: 0; box-sizing: border-box; }
  html, body {
    width: 1200px;
    height: 686px;
    overflow: hidden;
    background: var(--white);
  }
  .card {
    position: relative;
    width: 1200px;
    height: 686px;
    background: var(--paper);
    overflow: hidden;
    font-family: "Saira Semi Condensed", "Arial Narrow", sans-serif;
  }
  .card__frame {
    position: absolute;
    inset: 0;
    width: 100%;
    height: 100%;
  }
  .brand {
    position: absolute;
    left: 282px;
    top: 268px;
    display: flex;
    align-items: center;
    gap: 40px;
  }
  .brand__mark {
    width: 132px;
    height: 132px;
    background: var(--slate);
    flex: none;
  }
  .brand__text {
    display: flex;
    flex-direction: column;
    width: 462px;
  }
  .brand__name {
    color: var(--teal);
    font-weight: 600;
    font-size: 74px;
    line-height: 0.9;
    letter-spacing: 1px;
    white-space: nowrap;
  }
  .brand__division {
    display: flex;
    align-items: center;
    gap: 12px;
    margin-top: 14px;
    color: var(--teal);
    font-weight: 600;
    font-size: 16px;
    letter-spacing: 1.5px;
    white-space: nowrap;
  }
  .brand__division::before,
  .brand__division::after {
    content: "";
    flex: 1;
    height: 2px;
    background: var(--slate);
  }
  .brand__tagline {
    margin-top: 6px;
    color: var(--slate);
    font-weight: 500;
    font-size: 15px;
    letter-spacing: 9.6px;
    white-space: nowrap;
  }
</style>
</head>
<body>
  <main class="card">
    <svg class="card__frame" viewBox="0 0 1050 600" preserveAspectRatio="none" aria-hidden="true">
      <!-- top left corner -->
      <polygon fill="var(--slate)" points="0,0 206,0 0,214"/>
      <polygon fill="var(--teal)" points="200,0 1050,0 1050,19 218,19"/>
      <polygon fill="var(--teal)" points="198,24 213,24 10,238 5,238 5,229"/>
      <!-- bottom right corner -->
      <polygon fill="var(--slate)" points="0,578 850,578 830,600 0,600"/>
      <polygon fill="var(--slate)" points="836,574 852,574 1046,370 1046,356"/>
      <polygon fill="var(--teal)" points="848,600 1050,600 1050,382 1045,382"/>
    </svg>

    <section class="brand">
      <div class="brand__mark"></div>
      <div class="brand__text">
        <h1 class="brand__name">CEDAR RIDGE</h1>
        <p class="brand__division">PROPERTY GROUP</p>
        <p class="brand__tagline">ROOTED IN SERVICE</p>
      </div>
    </section>
  </main>
</body>
</html>
```